Beyond the Hunt Product Labeling

We need a label design for a new product we are launching. We have developed a cooking bag that will cook your fish or game bird instantly. This is for the everyday fisherman and upland game hunter. This label will be printed on a thin sticker on the front of a Mylar Bag. The Mylar Bag is 9 1/2 x 12 inches. Inside the Mylar Bag is 3 cooking bags.
Target Market(s)
hunters and fishermen
Industry/Entity Type
Cooking
Font styles to use
Sans Serif
Colors
Designer to choose colors to be used in the design.
Requirements
Must have
- It must have "Beyond the Hunt" logo. It should have Scale and Plume. Scale and Plume is the type of seasoning. It must have a small place on the label for net weight. It must also have the wording "Contains: 3 Individual Cooking Bags Inside.
Nice to have
- I really like a topographical map in the background. I have attached several images with products like that. It could also be cool having the background of the bag with a tiger trout's scales. I attached some images of that too. Some other ideas I thought i have is having a picture of the bird and fish on the bag. There is an GIF attached that has a cool looking fish that did that. There is also an image of a Holvak product that did the same thing.

```html
<!DOCTYPE html>
<html lang="en">
<head>
<meta charset="UTF-8">
<title>Beyond the Hunt – Scale &amp; Plume Label</title>
<link rel="stylesheet" href="https://fonts.googleapis.com/css2?family=Barlow+Condensed:wght@500;600;700&display=swap">
<style>
  :root {
    --page-bg: #ffffff;
    --label-black: #050607;
    --topo-line: #0f2a45;
    --water-deep: #0a2a5c;
    --water-mid: #1552a0;
    --water-light: #2a74c4;
    --orange-dark: #e2701f;
    --orange-light: #f2a56a;
    --ink: #1b1b1b;
    --white: #ffffff;
    --net-orange: #e8752a;
  }
  * { margin: 0; padding: 0; box-sizing: border-box; }
  html, body {
    width: 1200px;
    height: 1000px;
    overflow: hidden;
    background: var(--page-bg);
  }
  .canvas {
    position: relative;
    width: 1200px;
    height: 1000px;
    font-family: "Barlow Condensed", "Arial Narrow", sans-serif;
  }
  .label {
    position: absolute;
    left: 258px;
    top: 52px;
    width: 684px;
    height: 896px;
    border-radius: 16px;
    overflow: hidden;
    background: var(--label-black);
  }
  .topo-background {
    position: absolute;
    inset: 0;
    background:
      radial-gradient(ellipse at 20% 70%, rgba(20, 50, 85, 0.35), transparent 55%),
      radial-gradient(ellipse at 85% 30%, rgba(20, 50, 85, 0.3), transparent 50%),
      var(--label-black);
  }
  .water-panel {
    position: absolute;
    left: 115px;
    top: 115px;
    width: 455px;
    height: 380px;
    background: linear-gradient(160deg, var(--water-light) 0%, var(--water-mid) 40%, var(--water-deep) 100%);
  }
  .brand-name {
    position: absolute;
    left: 115px;
    top: 292px;
    width: 455px;
    text-align: center;
    color: var(--white);
    font-weight: 700;
    font-size: 52px;
    letter-spacing: 0.5px;
    line-height: 1;
  }
  .flavor-badge {
    position: absolute;
    left: 57px;
    top: 390px;
    width: 571px;
    height: 348px;
  }
  .flavor-badge svg { position: absolute; inset: 0; }
  .flavor-name {
    position: absolute;
    left: 0;
    right: 0;
    top: 58px;
    text-align: center;
    color: var(--ink);
    font-weight: 600;
    font-size: 104px;
    line-height: 0.98;
    letter-spacing: 1px;
  }
  .flavor-tagline {
    position: absolute;
    left: 0;
    right: 0;
    top: 264px;
    text-align: center;
    color: var(--ink);
    font-weight: 700;
    font-size: 27px;
    line-height: 1;
  }
  .contents-pill {
    position: absolute;
    left: 120px;
    top: 734px;
    width: 441px;
    height: 54px;
    border-radius: 16px;
    background: var(--white);
    color: var(--ink);
    font-weight: 700;
    font-size: 24px;
    display: flex;
    align-items: center;
    justify-content: center;
  }
  .net-weight {
    position: absolute;
    left: 0;
    right: 0;
    top: 800px;
    text-align: center;
    color: var(--net-orange);
    font-weight: 600;
    font-size: 17px;
  }
</style>
</head>
<body>
  <div class="canvas">
    <section class="label">
      <div class="topo-background" role="img" aria-label="Black background with faint blue topographic map contour lines"></div>
      <div class="water-panel" role="img" aria-label="Blue panel with rippling water-like wavy line pattern"></div>
      <div class="brand-name">BEYOND THE HUNT</div>

      <div class="flavor-badge">
        <svg width="571" height="348" viewBox="0 0 571 348" aria-hidden="true">
          <defs>
            <linearGradient id="badgeFill" x1="0" y1="0" x2="1" y2="0">
              <stop offset="0" stop-color="var(--orange-dark)"/>
              <stop offset="0.5" stop-color="var(--orange-light)"/>
              <stop offset="1" stop-color="var(--orange-dark)"/>
            </linearGradient>
          </defs>
          <path d="M4 76 L285.5 4 L567 76 L567 272 L285.5 344 L4 272 Z"
                fill="url(#badgeFill)" stroke="url(#badgeFill)" stroke-width="8" stroke-linejoin="round"/>
          <path d="M16 84 L285.5 15 L555 84 L555 264 L285.5 333 L16 264 Z"
                fill="none" stroke="#3a2312" stroke-width="1.2" stroke-linejoin="round"/>
        </svg>
        <div class="flavor-name">SCALE &amp;<br>PLUME</div>
        <div class="flavor-tagline">100% Natural Seasoning</div>
      </div>

      <div class="contents-pill">Contains: 3 Individual Cooking Bags Inside</div>
      <div class="net-weight">Net WT. 5.50 z</div>
    </section>
  </div>
</body>
</html>
```